Protrait photographers business card

Need a new catchy, chic business card to promote my new portrait photograghy business. Love taking the natural, location portraits of families, children, teens. It should look classy, but also warm & friendly. I want it to show that Famliy, friends, couples & childten are what I love photographing, so if it can have that sort of feel to it & also looking energetic.

Target Market(s)

Families, couples, babies, people on holidays wanting some locational professional photos

Industry/Entity Type

Portrait Photography

Contact Information for Business Card

Lumivale photography, By Tavi, Norah Balfrey,Ph: 0487356024, Kestrel cove, Qld

Font styles to use
Decorative
Script

Requirements
Must have
• Company name & photographers name
Nice to have
• a coloured card
Should not have
• not be on a white card

```html
<!DOCTYPE html>
<html lang="en">
<head>
<meta charset="utf-8">
<title>Lumivale Photography – Business Card</title>
<link rel="stylesheet" href="https://fonts.googleapis.com/css2?family=Cedarville+Cursive&family=Quicksand:wght@500;700&display=swap">
<style>
  :root {
    --page-bg: #ebebeb;
    --teal-edge: #17b2b1;
    --teal-deep: #05a8a7;
    --teal-mid: #7ccaca;
    --teal-glow: #d3ecec;
    --ink-light: #ffffff;
  }
  html, body {
    margin: 0;
    padding: 0;
    width: 1200px;
    height: 801px;
    overflow: hidden;
    background: var(--page-bg);
  }
  .business-card {
    position: absolute;
    left: 180px;
    top: 160px;
    width: 840px;
    height: 480px;
    background: linear-gradient(90deg,
      var(--teal-edge) 0%,
      var(--teal-mid) 22%,
      var(--teal-glow) 47%,
      var(--teal-mid) 62%,
      var(--teal-edge) 78%,
      var(--teal-deep) 100%);
    color: var(--ink-light);
    font-family: "Quicksand", sans-serif;
    box-shadow: 0 20px 40px rgba(0, 0, 0, 0.08);
  }
  .photographer-name {
    position: absolute;
    left: 80px;
    top: 150px;
    margin: 0;
    font-family: "Cedarville Cursive", cursive;
    font-weight: 400;
    font-size: 44px;
    line-height: 1.15;
    letter-spacing: 1px;
  }
  .contact-list {
    position: absolute;
    left: 205px;
    top: 295px;
    margin: 0;
    padding: 0;
    list-style: none;
    font-weight: 500;
    font-size: 22px;
    letter-spacing: 0.5px;
  }
  .contact-item {
    display: flex;
    align-items: center;
    gap: 16px;
    height: 50px;
  }
  .contact-icon {
    width: 24px;
    height: 24px;
    flex: none;
  }
  .studio-brand {
    position: absolute;
    left: 600px;
    top: 110px;
    width: 160px;
    display: flex;
    flex-direction: column;
    align-items: center;
    gap: 18px;
  }
  .brand-dot {
    width: 64px;
    height: 64px;
    border-radius: 50%;
    border: 4px solid var(--ink-light);
    box-sizing: border-box;
  }
  .studio-name {
    margin: 0;
    font-weight: 700;
    font-size: 26px;
    line-height: 1.05;
    text-transform: uppercase;
    text-align: center;
    letter-spacing: 0.5px;
  }
</style>
</head>
<body>
  <main class="business-card">
    <h1 class="photographer-name">Norah<br>Balfrey</h1>

    <ul class="contact-list">
      <li class="contact-item">
        <svg class="contact-icon" viewBox="0 0 24 24" aria-hidden="true">
          <path fill="#fff" d="M12 1.5a7.5 7.5 0 0 0-7.5 7.5c0 5.6 7.5 13.5 7.5 13.5s7.5-7.9 7.5-13.5A7.5 7.5 0 0 0 12 1.5zm0 10.3a2.8 2.8 0 1 1 0-5.6 2.8 2.8 0 0 1 0 5.6z"/>
        </svg>
        <span>Kestrel cove, Qld</span>
      </li>
      <li class="contact-item">
        <svg class="contact-icon" viewBox="0 0 24 24" aria-hidden="true">
          <circle cx="12" cy="12" r="10.5" fill="none" stroke="#fff" stroke-width="2"/>
          <path fill="#fff" d="M8.3 6.6c.4-.3.9-.2 1.2.2l1.2 1.8c.3.4.2.9-.1 1.2l-.8.7c.5 1.3 1.5 2.4 2.9 3.1l.7-.8c.3-.4.8-.4 1.2-.2l1.8 1.1c.4.3.5.8.3 1.2l-.6 1c-.5.8-1.5 1.1-2.4.8-3-1.1-5.3-3.5-6.3-6.5-.3-.9 0-1.9.8-2.4z"/>
        </svg>
        <span>Ph: 0487356024</span>
      </li>
    </ul>

    <div class="studio-brand">
      <div class="brand-dot" aria-hidden="true"></div>
      <p class="studio-name">Lumivale<br>Photography</p>
    </div>
  </main>
</body>
</html>
```